Redesign existing website

We would like a redesign of the website http://www.velbrisanalytics.com that creates a more modern, up to date look.

Velbris Analytics creates software for social science research and is focused on making the software user friendly and easy to use. We would like to convey seriousness, but also
a very up to date, just released look.

Feel free to modify the logo if you wish.

Target Market(s)

Academics, researchers

Industry/Entity Type

Software

Requirements
Must have
• The design should incorporate the same information as the current website.

```html
<!DOCTYPE html>
<html lang="en">
<head>
<meta charset="utf-8">
<title>Velbris Analytics</title>
<link rel="stylesheet" href="https://fonts.googleapis.com/css2?family=Arimo:wght@400&family=Cinzel:wght@400&family=Marcellus&display=swap">
<style>
:root{
  --brand-blue:#2447a0;
  --brand-blue-dark:#1b3886;
  --brand-blue-light:#3159b8;
  --ink:#1d3a86;
  --page:#f5f5f5;
  --rule:#dedede;
  --muted:#555;
  --white:#fff;
}
*{margin:0;padding:0;box-sizing:border-box}
html,body{width:1200px;height:742px;overflow:hidden;background:var(--page);font-family:Arimo,Arial,sans-serif}
.site{position:relative;width:1200px;height:742px}
.hero-photo{position:absolute;left:0;top:0;width:1200px;height:446px;
  background:linear-gradient(180deg,#c3d0dc 0%,#aebfce 45%,#8d8f74 100%)}
.contact-bar{position:absolute;top:14px;right:110px;display:flex;align-items:center;gap:20px;color:#2a3550;font-size:13px}
.contact-bar .phone{font-size:14px;letter-spacing:1.5px;display:flex;align-items:center;gap:8px}
.contact-bar .mail{display:flex;align-items:center;gap:7px}
.nav-band{position:absolute;left:0;top:50px;width:1200px;height:72px;
  background:linear-gradient(180deg,var(--brand-blue-light) 0%,var(--brand-blue) 45%,var(--brand-blue-dark) 100%)}
.main-nav{position:absolute;top:66px;right:103px;display:flex;height:38px}
.main-nav a{color:#e6ecfa;text-decoration:none;font-size:12px;letter-spacing:.2px;padding:0 13px;line-height:38px;border-left:1px solid #1a3278}
.main-nav a:first-child{border-left:none}
.brand-box{position:absolute;left:111px;top:14px;width:232px;height:144px;
  background:linear-gradient(180deg,#fff 0%,#ececec 100%);box-shadow:0 10px 14px -6px rgba(0,0,0,.45);
  display:flex;align-items:center;justify-content:center;gap:8px}
.brand-box .dot{width:16px;height:16px;border-radius:50%;background:var(--brand-blue)}
.brand-box .name{font-family:Marcellus,serif;font-size:22px;color:var(--brand-blue)}
.tagline{position:absolute;left:688px;top:165px;font-family:Cinzel,serif;color:var(--white);
  font-size:19.5px;line-height:24px;letter-spacing:.4px;text-shadow:1px 1px 2px rgba(0,0,0,.55)}
.login-band{position:absolute;left:0;top:446px;width:1200px;height:34px;
  background:linear-gradient(180deg,var(--brand-blue-light),var(--brand-blue-dark))}
.band-badge{position:absolute;left:562px;top:426px;width:76px;height:76px;border-radius:50%;
  background:linear-gradient(180deg,#ffffff,#d6d6d6);box-shadow:0 5px 6px rgba(0,0,0,.3);
  display:flex;align-items:center;justify-content:center}
.band-badge span{width:64px;height:64px;border-radius:50%;background:var(--brand-blue)}
.login-form{position:absolute;top:452px;left:779px;display:flex}
.login-form .field{width:118px;height:22px;background:#1a3485;border:1px solid #3e62c0;color:#6c8ee0;font-size:11px;padding-left:7px;line-height:20px}
.login-form .field+.field{margin-left:10px}
.login-form .submit{width:64px;height:22px;background:#2a4da8;border:1px solid #3e62c0;color:var(--white);font-size:11px;text-align:center;line-height:20px}
.intro{position:absolute;left:110px;top:509px;width:615px;color:var(--ink)}
.intro h1{font-family:Marcellus,serif;font-weight:400;font-size:23px;margin-bottom:16px}
.intro p{font-size:13px;line-height:18px;letter-spacing:.2px;margin-bottom:18px}
.divider{position:absolute;left:747px;top:514px;width:1px;height:126px;background:var(--rule)}
.product-card{position:absolute;left:776px;top:514px;width:314px}
.product-card .cap{height:8px;background:var(--brand-blue)}
.product-card .title{height:71px;background:linear-gradient(180deg,#d9d9d9 0%,#fafafa 45%,#e6e6e6 100%);
  font-family:Cinzel,serif;color:var(--brand-blue-dark);font-size:24px;text-align:center;line-height:76px}
.product-card .actions{display:flex;height:45px;background:var(--brand-blue)}
.product-card .actions a{color:var(--white);text-decoration:none;font-size:13px;letter-spacing:.3px;
  display:flex;align-items:center;gap:9px;padding-left:14px}
.product-card .actions a:first-child{width:151px}
.product-card .actions a+a{flex:1;border-left:1px solid #1a3278}
.product-card .shade{height:20px;background:radial-gradient(ellipse at top,rgba(0,0,0,.22),rgba(0,0,0,0) 70%)}
.footer-rule{position:absolute;left:100px;top:672px;width:980px;height:1px;background:var(--rule)}
.footer-nav{position:absolute;left:110px;top:691px;font-size:12px;color:var(--muted)}
.footer-nav span{margin:0 9px}
.copyright{position:absolute;right:110px;top:693px;font-size:11px;color:#444}
</style>
</head>
<body>
<div class="site">
  <div class="hero-photo" role="img" aria-label="Photo of a straight open road across grassland under a cloudy sky"></div>

  <div class="contact-bar">
    <span class="phone">
      <svg width="14" height="18" viewBox="0 0 14 18"><path d="M3 1l3 4-2 2c1 3 2 5 4 6l2-2 3 3-2 3C5 16 1 9 1 3z" fill="#2447a0"/></svg>
      626 - 555-0187
    </span>
    <span class="mail">
      <svg width="16" height="16" viewBox="0 0 16 16"><circle cx="8" cy="8" r="6.5" fill="none" stroke="#2447a0" stroke-width="1.6"/><circle cx="8" cy="8" r="2.5" fill="none" stroke="#2447a0" stroke-width="1.6"/></svg>
      info@velbrisanalytics.com
    </span>
  </div>

  <div class="nav-band"></div>
  <nav class="main-nav">
    <a href="#">HOME</a><a href="#">ABOUT US</a><a href="#">PRODUCTS</a><a href="#">NEWS</a><a href="#">CONTACT US</a>
  </nav>

  <div class="brand-box"><span class="dot"></span><span class="name">Velbris Analytics</span></div>

  <p class="tagline">Increasing<br>the power and efficiency<br>of empirical social science research</p>

  <div class="login-band"></div>
  <div class="band-badge"><span></span></div>
  <div class="login-form">
    <div class="field">User Name</div>
    <div class="field">Password</div>
    <div class="submit">Login</div>
  </div>

  <section class="intro">
    <h1>Welcome to Velbris Analytics</h1>
    <p>The mission of Velbris Analytics, Inc. is to produce software products that multiply the power and efficiency of empirical scientific research in the social sciences.</p>
    <p>A central goal is to expand access to complex data sources and to the advanced methods of scientific investigation needed to analyze them.</p>
  </section>

  <div class="divider"></div>

  <aside class="product-card">
    <div class="cap"></div>
    <div class="title">Velbris Data Manager</div>
    <div class="actions">
      <a href="#"><svg width="9" height="10" viewBox="0 0 9 10"><path d="M0 0l9 5-9 5z" fill="#fff"/></svg>Preview Release</a>
      <a href="#"><svg width="11" height="9" viewBox="0 0 11 9"><path d="M0 0h11L5.5 9z" fill="#fff"/></svg>Download Release</a>
    </div>
    <div class="shade"></div>
  </aside>

  <div class="footer-rule"></div>
  <footer class="footer-nav">Home<span>|</span>About Us<span>|</span>Products<span>|</span>News<span>|</span>Contact Us</footer>
  <div class="copyright">Copyright © 2011 velbrisanalytics.com.</div>
</div>
</body>
</html>
```